New Crumvello Poster

This is for designer Doreen ONLY.<br/><br/>hi doreen,<br/><br/>Hope you are well.<br/>I need to redo my Crumvello combo. <br/>So the layout I want is clean and simple. <br/>Photo is on the left hand side, then combo's details and price.<br/>Same poster size.<br/>Thank you<br/><br/><br/>Pho Combo: 1x Pho + 1x Side + 1x Drinks = $23<br/>Noodle Salad Combo: 1x Noodle Salads + 1x Side + 1x Drinks = $23<br/>Rice Combo: 1x Rice + 1x Side + 1x Drinks = $25<br/>Combo for 2: 2x mains + 1x side + 2x Drinks = $39<br/>Family Combo: 4x mains + 2 sides + 4x Drinks = 79

```html
<!DOCTYPE html>
<html lang="en">
<head>
<meta charset="utf-8">
<title>Crumvello Combo Poster</title>
<link href="https://fonts.googleapis.com/css2?family=Questrial&family=Josefin+Sans:wght@400&family=Cutive&display=swap" rel="stylesheet">
<style>
  :root {
    --backdrop: #626d76;
    --board: #1b1613;
    --board-light: #2a221d;
    --copper: #d98a5c;
    --gold: #f0a61e;
    --ink: #f4f1ec;
    --rule-light: #e9e5df;
    --rule-gold: #e29a1c;
  }
  * { margin: 0; padding: 0; box-sizing: border-box; }
  html, body {
    width: 1008px; height: 1200px; overflow: hidden;
    background: var(--backdrop);
  }
  .poster {
    position: absolute; left: 84px; top: 0;
    width: 840px; height: 1200px;
    background:
      repeating-linear-gradient(90deg, rgba(255,255,255,0.015) 0 3px, rgba(0,0,0,0.05) 3px 7px),
      radial-gradient(ellipse at 40% 30%, var(--board-light), var(--board) 70%);
    overflow: hidden;
  }
  .photo {
    position: absolute; border-radius: 14px;
    background: radial-gradient(ellipse at 50% 50%, #e7e3dc 0%, #b59a74 35%, #5a3d26 65%, rgba(27,22,19,0) 80%);
  }
  .v-rule {
    position: absolute; width: 0;
    border-left: 2px dotted var(--rule-light);
  }
  .h-rule {
    position: absolute; height: 0;
    border-top: 2px dotted var(--rule-gold);
    left: 34px; width: 772px;
  }
  .combo-title {
    position: absolute; font-family: "Questrial", sans-serif;
    color: var(--copper); font-size: 37px; line-height: 42px; letter-spacing: 1px;
  }
  .combo-items {
    position: absolute; font-family: "Josefin Sans", sans-serif;
    color: var(--ink); font-size: 19px; line-height: 42px; white-space: nowrap;
    border-top: 2px dotted var(--rule-light);
    border-bottom: 2px dotted var(--rule-light);
    padding-top: 2px;
  }
  .combo-price {
    position: absolute; font-family: "Cutive", serif;
    color: var(--gold); font-size: 52px; line-height: 60px;
  }
  .center { text-align: center; }
  .double-rule {
    position: absolute; left: 405px; top: 833px; width: 13px; height: 310px;
    border-left: 3px dotted var(--rule-light);
    border-right: 3px dotted var(--rule-light);
  }
</style>
</head>
<body>
<main class="poster">
  <!-- Pho combo -->
  <div class="photo" style="left:77px;top:40px;width:230px;height:221px" role="img" aria-label="Photo of a bowl of pho, a side plate of fried food and a bottled iced tea"></div>
  <div class="v-rule" style="left:367px;top:27px;height:246px"></div>
  <h2 class="combo-title" style="left:392px;top:60px">PHO COMBO</h2>
  <p class="combo-items" style="left:392px;top:122px;width:292px">1X PHO + 1X SIDE + 1X DRINKS</p>
  <p class="combo-price" style="left:396px;top:182px">$23</p>
  <div class="h-rule" style="top:300px"></div>

  <!-- Noodle salad combo -->
  <div class="photo" style="left:112px;top:329px;width:167px;height:229px" role="img" aria-label="Photo of a noodle salad bowl, fresh rice paper rolls with dipping sauce and a bottled drink"></div>
  <div class="v-rule" style="left:367px;top:322px;height:247px"></div>
  <h2 class="combo-title" style="left:392px;top:326px">NOODLE SALAD<br>COMBO</h2>
  <p class="combo-items" style="left:392px;top:429px;width:396px">1X NOODLE SALADS + 1X SIDE + 1X DRINKS</p>
  <p class="combo-price" style="left:392px;top:488px">$23</p>
  <div class="h-rule" style="top:585px"></div>

  <!-- Rice combo -->
  <div class="photo" style="left:112px;top:612px;width:208px;height:166px" role="img" aria-label="Photo of a rice plate with stir-fry, spring rolls with dipping sauce and a bottled drink"></div>
  <div class="v-rule" style="left:367px;top:603px;height:198px"></div>
  <h2 class="combo-title" style="left:392px;top:604px">RICE COMBO</h2>
  <p class="combo-items" style="left:392px;top:671px;width:292px">1X RICE + 1X SIDE + 1X DRINKS</p>
  <p class="combo-price" style="left:392px;top:730px">$25</p>
  <div class="h-rule" style="top:817px"></div>

  <!-- Combo for 2 -->
  <div class="photo" style="left:77px;top:833px;width:283px;height:180px" role="img" aria-label="Photo of pho, a tofu noodle bowl, spring rolls and two bottled drinks"></div>
  <div class="double-rule"></div>
  <h2 class="combo-title center" style="left:34px;top:1018px;width:360px">COMBO FOR 2</h2>
  <p class="combo-items center" style="left:72px;top:1070px;width:290px">2X MAINS + 1X SIDE + 2X DRINKS</p>
  <p class="combo-price center" style="left:34px;top:1123px;width:360px">$39</p>

  <!-- Family combo -->
  <div class="photo" style="left:464px;top:842px;width:319px;height:157px" role="img" aria-label="Photo of four main dishes, spring rolls, rice paper rolls and four bottled drinks"></div>
  <h2 class="combo-title center" style="left:430px;top:1018px;width:396px">FAMILY COMBO</h2>
  <p class="combo-items center" style="left:484px;top:1070px;width:290px">4X MAINS + 2 SIDES + 4X DRINKS</p>
  <p class="combo-price center" style="left:430px;top:1123px;width:396px">$79</p>
</main>
</body>
</html>
```